Journeys With Marcella Business Cards

I need a business card design for my upscale Travel Agency.
Attached you can find my logo.
I would like to include the following:
- Name
- Title
- Phone Number
- Email
- Website
- and then something like: Follow us: JourneysWithMarcella (and then social media icons in color).
The logo should be in the front and then also the back.
I am also attaching a design that I liked (mostly for the layout) but open to any suggestions
Industry/Entity Type
Travel Agent
Contact Information for Business Card
Name: Marcella Dorn
Title: Travel Designer / Owner
Phone: 415-927-3308
Email: marcella@journeyswithmarcella-example.com
Website: www.JourneysWithMarcella-example.com
Social Media Handles for FB,IG, Twitter: JourneysWithMarcella
Colors
Designer to choose colors to be used in the design.
Look and feel

```html
<!DOCTYPE html>
<html lang="en">
<head>
<meta charset="utf-8">
<title>Journeys With Marcella Business Cards</title>
<link href="https://fonts.googleapis.com/css2?family=Open+Sans:wght@400;600;700&display=swap" rel="stylesheet">
<style>
  :root {
    --backdrop: #e4e4e4;
    --card: #f7f7f7;
    --card-edge: #e9e9e9;
    --accent: #e89a4c;
    --ink: #1f1f1f;
    --rule: #b9b9b9;
  }
  * { box-sizing: border-box; margin: 0; padding: 0; }
  html, body { width: 1200px; height: 1021px; overflow: hidden; }
  body {
    background: var(--backdrop);
    font-family: "Open Sans", Arial, sans-serif;
    color: var(--ink);
    position: relative;
  }
  .card {
    position: absolute;
    left: 220px;
    width: 760px;
    height: 434px;
    background: linear-gradient(135deg, #ffffff 0%, var(--card) 55%, var(--card-edge) 100%);
    border-radius: 26px;
    box-shadow: 0 8px 22px rgba(0,0,0,0.18);
  }
  .card-front { top: 52px; }
  .card-back { top: 535px; }

  .brand {
    display: flex;
    align-items: center;
    gap: 14px;
    color: var(--accent);
    font-weight: 600;
  }
  .brand-square {
    width: 26px; height: 26px;
    background: var(--accent);
    flex: none;
  }
  .card-front .brand {
    position: absolute;
    top: 170px; left: 0; right: 0;
    justify-content: center;
    font-size: 36px;
  }
  .card-front .brand .brand-square { width: 34px; height: 34px; }
  .front-url {
    position: absolute;
    bottom: 48px; left: 0; right: 0;
    text-align: center;
    font-size: 18px;
    font-weight: 600;
  }
  .front-url .accent { color: var(--accent); }

  .card-back .brand {
    position: absolute;
    top: 128px; left: 40px;
    font-size: 22px;
  }
  .divider {
    position: absolute;
    left: 362px; top: 90px;
    width: 1px; height: 150px;
    background: var(--rule);
  }
  .contact {
    position: absolute;
    left: 388px; top: 100px;
    right: 24px;
  }
  .contact-name {
    color: var(--accent);
    font-weight: 700;
    font-size: 24px;
    line-height: 1.1;
  }
  .contact-title {
    font-size: 17px;
    margin-bottom: 14px;
  }
  .contact-list { list-style: none; }
  .contact-list li {
    display: flex;
    align-items: center;
    gap: 9px;
    font-size: 15px;
    line-height: 1.75;
    white-space: nowrap;
  }
  .contact-list svg { width: 15px; height: 15px; flex: none; }
  .social {
    position: absolute;
    left: 40px; bottom: 92px;
    width: 300px;
    text-align: center;
  }
  .social-handle {
    display: inline-flex;
    align-items: center;
    gap: 8px;
    font-size: 18px;
  }
  .social-square {
    width: 12px; height: 12px;
    background: var(--accent);
  }
</style>
</head>
<body>
  <section class="card card-front" aria-label="Card front">
    <div class="brand"><span class="brand-square"></span><span>Journeys With Marcella</span></div>
    <p class="front-url">www.<span class="accent">JourneysWithMarcella-example</span>.com</p>
  </section>

  <section class="card card-back" aria-label="Card back">
    <div class="brand"><span class="brand-square"></span><span>Journeys With Marcella</span></div>
    <div class="divider"></div>
    <div class="contact">
      <p class="contact-name">Marcella Dorn</p>
      <p class="contact-title">Travel Designer / Owner</p>
      <ul class="contact-list">
        <li>
          <svg viewBox="0 0 16 16" aria-hidden="true"><path d="M3.5 1.5 L6 1.5 L7 5 L5.4 6.3 C6.3 8.2 7.8 9.7 9.7 10.6 L11 9 L14.5 10 L14.5 12.5 C14.5 13.6 13.6 14.5 12.5 14.5 C6.5 14.5 1.5 9.5 1.5 3.5 C1.5 2.4 2.4 1.5 3.5 1.5 Z" fill="var(--accent)"/></svg>
          415-927-3308
        </li>
        <li>
          <svg viewBox="0 0 16 16" aria-hidden="true"><rect x="1.5" y="3.5" width="13" height="9" fill="none" stroke="var(--accent)" stroke-width="1.4"/><path d="M1.5 3.5 L8 9 L14.5 3.5" fill="none" stroke="var(--accent)" stroke-width="1.4"/></svg>
          marcella@journeyswithmarcella-example.com
        </li>
        <li>
          <svg viewBox="0 0 16 16" aria-hidden="true"><g fill="none" stroke="var(--accent)" stroke-width="1.3"><circle cx="8" cy="8" r="6.5"/><ellipse cx="8" cy="8" rx="3" ry="6.5"/><line x1="1.5" y1="8" x2="14.5" y2="8"/></g></svg>
          www.JourneysWithMarcella-example.com
        </li>
      </ul>
    </div>
    <div class="social">
      <span class="social-handle"><span class="social-square"></span>JourneysWithMarcella</span>
    </div>
  </section>
</body>
</html>
```